Cloud backup company needs a new website

We need a new design for our website as the current one is quite dated now. You can view the current website at www.vellostrand-files.net.au to view the content elements.

We provide cloud backup services (ie remote off site to a cluster of servers) to small to medium businesses looking for better alternatives to tape or optical media backups.

Target Market(s)

SME/SMB (Businesses with fewer than 100 employees)

Industry/Entity Type

It Company

Requirements
Must have
• Must have sections to sign up to newsletter, log in to account, view news feed as per current website.

Must have a prominent call to action to sign up for a trial and view pricing.

Also like it to have twitter and facebook links/likes integration
Should not have
• No Flash, no serif fonts

```html
<!DOCTYPE html>
<html lang="en">
<head>
<meta charset="utf-8">
<title>Vellostrand – Remote Backup</title>
<link href="https://fonts.googleapis.com/css2?family=Open+Sans:wght@400;600&family=Quicksand:wght@600;700&display=swap" rel="stylesheet">
<style>
:root{
  --orange:#f07d1a;
  --orange-light:#f7a23c;
  --orange-dark:#d9660b;
  --text:#555;
  --text-dark:#333;
  --line:#dcdcdc;
  --footer:#4b4b4b;
  --white:#fff;
}
*{margin:0;padding:0;box-sizing:border-box}
html,body{width:960px;height:1200px;overflow:hidden}
body{position:relative;background:var(--white);font-family:"Open Sans",Arial,sans-serif;color:var(--text)}
.abs{position:absolute}
.site-header{left:0;top:0;width:960px;height:170px;background:linear-gradient(#fff,#ececec);border-bottom:1px solid #d0d0d0}
.orange-band{left:0;top:170px;width:960px;height:70px;background:linear-gradient(var(--orange-dark),var(--orange-light))}
.nav-pointer{left:372px;top:164px;width:0;height:0;border-left:6px solid transparent;border-right:6px solid transparent;border-bottom:7px solid var(--orange-dark)}
.login-box{left:482px;top:26px;width:358px;height:61px;border:1px solid #ddd;border-radius:5px;background:#f3f3f3}
.login-box .user-icon{left:12px;top:11px}
.field{height:23px;width:120px;top:7px;background:#fff;border:1px solid #ccc;font-size:8px;color:#777;padding:6px 7px}
.field.user{left:33px}.field.pass{left:159px}
.btn{background:linear-gradient(var(--orange-light),var(--orange));color:#fff;border:1px solid var(--orange-dark);border-radius:4px;text-align:center}
.login-btn{left:287px;top:8px;width:59px;height:21px;font-size:9px;line-height:19px}
.login-link{top:46px;font-size:8px;color:var(--orange)}
.logo{left:120px;top:120px;width:188px;height:32px;background:#fff;font-size:22px;font-weight:400;color:var(--orange);line-height:32px;padding-left:2px;letter-spacing:-0.5px}
.main-nav{top:119px;font-size:9.5px;color:var(--text-dark);letter-spacing:.2px}
.hero{left:120px;top:194px;width:720px;height:234px;background:linear-gradient(#fafafa,#e4e4e4);box-shadow:0 12px 12px -8px rgba(0,0,0,.35)}
.hero h1{left:27px;top:30px;width:270px;font-family:"Quicksand",sans-serif;font-weight:700;font-variant:small-caps;font-size:16px;line-height:23px;letter-spacing:1.5px;color:var(--orange)}
.hero p{left:27px;width:320px;font-size:7.5px;line-height:13.6px}
.hero-btn{left:27px;top:164px;width:134px;height:27px;font-size:10px;line-height:25px}
.hero-art{left:366px;top:34px;width:354px;height:180px;background:linear-gradient(100deg,rgba(239,231,218,0) 0%,#f1e4c9 22%,#f2c35e 45%,#b9b6ad 72%,#46535c 100%);opacity:.85}
.slider-nav{left:664px;top:34px;width:36px;height:14px;border:1px solid #ccc;border-radius:7px;background:#eee}
.how{left:118px;top:482px;width:722px;height:235px;border:1px solid var(--line);box-shadow:0 10px 10px -8px rgba(0,0,0,.25)}
.how-title{left:382px;top:472px;width:196px;background:#fff;text-align:center;font-size:13.5px;color:var(--text-dark);font-weight:400}
.how-sub{left:380px;top:496px;width:200px;text-align:center;font-size:8.5px;color:var(--orange)}
.step{width:170px;text-align:center}
.step h3{font-family:"Quicksand",sans-serif;font-weight:700;font-variant:small-caps;font-size:12px;letter-spacing:1px;color:var(--orange);height:16px}
.step .num{display:inline-block;width:14px;height:14px;border-radius:50%;background:var(--orange);color:#fff;font-size:8px;line-height:14px;margin-right:6px;vertical-align:1px;font-family:"Open Sans",sans-serif}
.step .icon{margin:21px auto 0;width:76px;height:70px}
.step p{margin-top:28px;font-size:7.8px;line-height:13.6px;color:var(--text-dark)}
.step p .accent{color:var(--orange)}
.cta-text{left:190px;top:752px;font-size:12px;color:var(--text-dark)}
.cta-btn{left:570px;top:746px;width:149px;height:35px;font-size:13px;line-height:33px;border-radius:6px}
.section-title{font-size:13.5px;color:var(--text-dark);top:819px;font-weight:400}
.kicker{font-family:"Quicksand",sans-serif;font-weight:700;font-variant:small-caps;font-size:11px;letter-spacing:1px;color:var(--orange)}
.about p{left:120px;width:462px;font-size:9px;line-height:16.4px;color:#666;text-align:justify}
.news-item .thumb{left:606px;width:59px;height:50px;border:2px solid #fff;box-shadow:0 1px 3px rgba(0,0,0,.4)}
.news-item .kicker{left:675px;width:150px;line-height:13px;font-size:10px}
.news-item p{left:677px;width:150px;font-size:8.5px;line-height:13.6px;color:#666;text-align:justify}
.site-footer{left:0;top:1107px;width:960px;height:93px;background:var(--footer);color:#eee}
.footer-links{left:120px;top:20px;font-size:8.5px}
.copyright{left:119px;top:55px;font-size:8.5px}
.social-title{left:441px;top:19px;font-size:9.5px}
.social{top:49px;width:20px;height:20px;border-radius:50%;background:#bbb}
.newsletter-title{left:611px;top:17px;font-size:12px}
.newsletter-title span{font-size:10px}
.newsletter-input{left:613px;top:48px;width:146px;height:26px;background:linear-gradient(#999,#bbb);border-radius:3px 0 0 3px}
.newsletter-btn{left:759px;top:48px;width:67px;height:26px;background:linear-gradient(#fff,#ddd);color:#333;font-size:9px;line-height:26px;text-align:center;border-radius:0 3px 3px 0}
</style>
</head>
<body>

<header class="site-header abs">
  <div class="login-box abs">
    <svg class="user-icon abs" width="10" height="13" viewBox="0 0 10 13"><circle cx="5" cy="3.5" r="3" fill="#f07d1a"/><rect x="0" y="7" width="10" height="6" rx="2" fill="#f07d1a"/></svg>
    <div class="field user abs">Username :</div>
    <div class="field pass abs">Password :</div>
    <div class="btn login-btn abs">Log in</div>
    <div class="login-link abs" style="left:161px">Forgot password?</div>
    <div class="login-link abs" style="left:265px">Create New Account</div>
  </div>
  <div class="logo abs">vellostrand</div>
  <nav>
    <span class="main-nav abs" style="left:369px">HOME</span>
    <span class="main-nav abs" style="left:426px">SOLUTIONS</span>
    <span class="main-nav abs" style="left:506px">SERVICES</span>
    <span class="main-nav abs" style="left:579px">SUPPORT</span>
    <span class="main-nav abs" style="left:651px">PARTNERS</span>
    <span class="main-nav abs" style="left:728px">ABOUT</span>
    <span class="main-nav abs" style="left:790px">DOWNLOAD</span>
  </nav>
</header>
<div class="nav-pointer abs"></div>
<div class="orange-band abs"></div>

<section class="hero abs">
  <h1 class="abs">Suddenly lost all of your computer data?</h1>
  <p class="abs" style="top:87px">Lorem Ipsum is simply dummy text of the printing and typesetting industry. Lorem Ipsum has been the industry's standard dummy text ever since the 1500s.</p>
  <p class="abs" style="top:128px">It was popularised in the 1960s with the release of Letraset sheets containing Lorem Ipsum passages, and more.</p>
  <div class="btn hero-btn abs">Download Trail Now</div>
  <div class="hero-art abs" role="img" aria-label="Illustration of an open box of folders with a magnifying glass over binary code reading theft"></div>
  <div class="slider-nav abs">
    <svg width="36" height="14" viewBox="0 0 36 14"><path d="M13 4 L9 7 L13 10Z" fill="#f07d1a"/><line x1="17" y1="2" x2="17" y2="12" stroke="#ccc"/><path d="M21 4 L25 7 L21 10Z" fill="#f07d1a"/></svg>
  </div>
</section>

<section>
  <div class="how abs"></div>
  <h2 class="how-title abs">How Vellostrand Works</h2>
  <div class="how-sub abs">it really is that simple</div>

  <div class="step abs" style="left:123px;top:528px">
    <h3><span class="num">1</span>Install</h3>
    <div class="icon" role="img" aria-label="Software box with a disc" style="background:linear-gradient(135deg,#e8e8e8,#9fb6c8)"></div>
    <p style="margin-top:30px">Lorem Ipsum is simply dummy text of the printing and typesetting industry. Lorem Ipsum.</p>
  </div>
  <div class="step abs" style="left:305px;top:528px">
    <h3><span class="num">2</span>Create Backup</h3>
    <div class="icon" role="img" aria-label="Gear with a blue refresh arrow" style="background:linear-gradient(135deg,#e4e4e4,#9cb3cf)"></div>
    <p>Lorem Ipsum is simply dummy text of the printing and typesetting industry. Lorem Ipsum.</p>
  </div>
  <div class="step abs" style="left:489px;top:528px">
    <h3><span class="num">3</span>Schedule Backup</h3>
    <div class="icon" role="img" aria-label="Server tower with a clock" style="background:linear-gradient(135deg,#3a3a3a,#9a9a9a)"></div>
    <p>Lorem Ipsum is simply dummy text of the printing and typesetting industry. Lorem Ipsum.</p>
  </div>
  <div class="step abs" style="left:672px;top:528px">
    <h3><span class="num">4</span>Restore</h3>
    <div class="icon" role="img" aria-label="Hard drive with a restore arrow" style="background:linear-gradient(135deg,#ddd,#888 60%,#5a8fc0)"></div>
    <p style="margin-top:26px">Lorem Ipsum is simply dummy text of the printing and typesetting.<br><span class="accent">it really is that simple</span></p>
  </div>
</section>

<p class="cta-text abs">Try a no obligation 14 day test drive of our remote backup system.</p>
<div class="btn cta-btn abs">Download Trail Now</div>

<section class="about">
  <h2 class="section-title abs" style="left:118px">Offsite Backup Experts</h2>
  <h3 class="kicker abs" style="left:119px;top:849px">How much could you afford to lose?</h3>
  <p class="abs" style="top:880px">Most companies believe their critical data is adequately protected from a catastrophic event – until something happens. Is this really how you plan to determine whether or not your business continuity management or disaster recovery plan is 100% effective?</p>
  <p class="abs" style="top:946px">For the Small to Medium Business Enterprise (SME), any event that wipes out all information could easily be the end of that business. As a result, no business can afford to cut corners when it comes to protecting their data from any unforeseen event.</p>
  <p class="abs" style="top:1012px">Offsite Backup is a fundamental disaster recovery requirement of any sized business or any professional in a sole practice that uses computers to store information.</p>
</section>

<section class="news">
  <h2 class="section-title abs" style="left:606px">Latest News</h2>
  <article class="news-item">
    <div class="thumb abs" style="top:854px;background:linear-gradient(#cfd4d8,#4a4f55)" role="img" aria-label="Photo of a businessman in a suit"></div>
    <h3 class="kicker abs" style="top:850px">Are you ready for your server to fail?</h3>
    <p class="abs" style="top:880px">What would you do if you walked into your office tomorrow morning, switched on your ...</p>
  </article>
  <article class="news-item">
    <div class="thumb abs" style="top:950px;background:linear-gradient(#2f7fc6,#9cc8e6 60%,#6aa33a)" role="img" aria-label="Photo of a man facing a sky of floating icons"></div>
    <h3 class="kicker abs" style="top:948px;left:677px">Remote, Offsite Backup a Great Value</h3>
    <p class="abs" style="top:978px">The idea of sending mission critical data over the Internet was a scary proposition for ...</p>
  </article>
</section>

<footer class="site-footer abs">
  <div class="footer-links abs">Sitemap &nbsp;|&nbsp; Terms &nbsp;|&nbsp; Privacy</div>
  <div class="copyright abs">Copyright © 2013. All Rights Reserved</div>
  <div class="social-title abs">Social Media</div>
  <div class="social abs" style="left:441px" aria-label="Social link"></div>
  <div class="social abs" style="left:468px" aria-label="Social link"></div>
  <div class="newsletter-title abs">Stay Connected. <span>Sign up for newsletter.</span></div>
  <div class="newsletter-input abs"></div>
  <div class="newsletter-btn abs">Sign Up</div>
</footer>

</body>
</html>
```